Letterhead Design

We need a new Letterhead design for a 30 year old Electrical Company. We service domestic and commercial places. We have a logo recently made so to incorporate that. Using same colours or interested to see others added.
Would like to see a couple of options with all the info in letterhead, then another with info in a footnote down the bottom.

info needed to be added:

-Lic. No 48162
8/22-24 Larkin Rd, Tolvern 2087
W - brightcoilpower.com.au
T - (02) 9471 3825
M - 0427 593 168
E - info@brightcoilpower.com.au
ABN: 42 597 214 630

Electrical

```html
<!DOCTYPE html>
<html lang="en">
<head>
<meta charset="utf-8">
<title>Brightcoil Power – Letterhead</title>
<link rel="stylesheet" href="https://fonts.googleapis.com/css2?family=Jost:wght@300;400;500&display=swap">
<style>
  :root {
    --backdrop: #e6e7e9;
    --paper: #ffffff;
    --paper-edge: #6d6e70;
    --ink: #1f2f3a;
    --ink-soft: #55585c;
    --accent: #f7982a;
  }
  * { margin: 0; padding: 0; box-sizing: border-box; }
  html, body {
    width: 1200px;
    height: 848px;
    overflow: hidden;
    background: var(--backdrop);
    font-family: "Jost", "Futura", sans-serif;
  }
  .canvas {
    position: relative;
    width: 1200px;
    height: 848px;
  }
  .letterhead {
    position: absolute;
    left: 389px;
    top: 158px;
    width: 376px;
    height: 532px;
    background: var(--paper);
    border: 1px solid var(--paper-edge);
  }
  .brand {
    position: absolute;
    left: 29px;
    top: 47px;
    font-weight: 500;
    font-size: 17px;
    line-height: 1;
    color: var(--ink);
    letter-spacing: 0.2px;
  }
  .contact {
    position: absolute;
    left: 33px;
    top: 125px;
    list-style: none;
    font-size: 5.4px;
    line-height: 9.3px;
    color: var(--ink);
  }
  .contact .muted {
    font-weight: 300;
    color: var(--ink-soft);
  }
  .contact .address {
    font-weight: 300;
    color: var(--ink-soft);
    font-size: 5.8px;
  }
  .contact .label {
    color: var(--accent);
    font-weight: 500;
    margin-right: 2px;
  }
  .contact .strong { font-weight: 500; }
  .contact .web {
    color: var(--accent);
    letter-spacing: 0.3px;
  }
  .footer-band {
    position: absolute;
    left: 0;
    bottom: 0;
    width: 100%;
    height: 19px;
    background: var(--accent);
  }
</style>
</head>
<body>
  <main class="canvas">
    <article class="letterhead">
      <h1 class="brand">Brightcoil Power</h1>
      <ul class="contact">
        <li class="muted">Lic. No 48162</li>
        <li class="address">8/22-24 Larkin Rd, Tolvern 2087</li>
        <li class="strong"><span class="label">T</span>(02) 9471 3825</li>
        <li class="strong"><span class="label">M</span>0427 593 168</li>
        <li><span class="label">E</span>info@brightcoilpower.com.au</li>
        <li class="web">www.brightcoilpower.com.au</li>
        <li class="muted">ABN: 42 597 214 630</li>
      </ul>
      <div class="footer-band"></div>
    </article>
  </main>
</body>
</html>
```